KRV Affirmation and Intention Card Design

I would like to have designs created that will be used on my Affirmation and Intention Cards I will be selling. We are a luxury brand. The designs need to be aesthetically pleasing, but minimal (think blush pinks/matte blacks/cream/warm earth tones/teals with gold/rose gold/silver lettering and visuals. Intention cards will have the same intentions as the inspiration photo. Affirmation cards will have random inspirational and biblical quotes. I only need two designs for the back of the Affirmation cards. One for design for every day quotes and one design for biblical quotes. For the intentions cards I would like a design for one side of card that will be on all cards and on the other side a design that correlates with each intention. See inspiration photo attached.

Target Market(s)

Millennials/ Women/ Similiar to Inspiration Photos below. Design that will look well on any color card stock I choose.

Industry/Entity Type

Lifestyle

Requirements
Must have
• Design that can fit on cards approximately 4 x 2.5 or 4x3 or 3.5 x 2.5 in size

```html
<!DOCTYPE html>
<html lang="en">
<head>
<meta charset="utf-8">
<title>Affirmation Cards – Biblical</title>
<link href="https://fonts.googleapis.com/css2?family=Tenor+Sans&family=Poiret+One&display=swap" rel="stylesheet">
<style>
  :root {
    --backdrop: #ebebeb;
    --card-blush: #f4cdc2;
    --art-blush: #eab9ad;
    --ink: #333132;
  }
  html, body {
    margin: 0;
    padding: 0;
    width: 1200px;
    height: 1200px;
    overflow: hidden;
    background: var(--backdrop);
  }
  .canvas {
    position: relative;
    width: 1200px;
    height: 1200px;
  }
  .card {
    position: absolute;
    top: 242px;
    width: 448px;
    height: 716px;
    background: var(--card-blush);
    border-radius: 13px;
  }
  .card--front { left: 120px; }
  .card--back { left: 632px; }
  .card-lines {
    position: absolute;
    inset: 0;
    width: 448px;
    height: 716px;
  }
  .cross-art {
    position: absolute;
    left: 66px;
    top: 113px;
    width: 307px;
    height: 426px;
    border-radius: 8px;
    background: radial-gradient(ellipse at 50% 40%, var(--art-blush) 0%, rgba(234,185,173,0.35) 60%, rgba(234,185,173,0) 100%);
  }
  .card-category {
    position: absolute;
    left: 0;
    right: 0;
    top: 595px;
    margin: 0;
    text-align: center;
    font-family: "Tenor Sans", sans-serif;
    font-weight: 400;
    font-size: 48px;
    line-height: 60px;
    color: var(--ink);
  }
  .verse-reference {
    position: absolute;
    left: 0;
    right: 0;
    top: 106px;
    margin: 0;
    text-align: center;
    font-family: "Tenor Sans", sans-serif;
    font-weight: 400;
    font-size: 37px;
    line-height: 42px;
    color: var(--ink);
  }
  .verse-text {
    position: absolute;
    left: 20px;
    right: 20px;
    top: 212px;
    margin: 0;
    text-align: center;
    white-space: nowrap;
    font-family: "Poiret One", sans-serif;
    font-size: 35px;
    line-height: 35.3px;
    letter-spacing: 1px;
    color: var(--ink);
  }
</style>
</head>
<body>
<main class="canvas">

  <section class="card card--front" aria-label="Biblical affirmation card, front">
    <svg class="card-lines" viewBox="0 0 448 716" aria-hidden="true">
      <rect x="47" y="49" width="354" height="510" rx="12" fill="none" stroke="var(--ink)" stroke-width="1.3"/>
      <circle cx="224" cy="291" r="197" fill="none" stroke="var(--ink)" stroke-width="1.4"/>
    </svg>
    <div class="cross-art" role="img" aria-label="Illustration of a radiant cross with light rays and scattered sparkle stars"></div>
    <h2 class="card-category">Biblical</h2>
  </section>

  <section class="card card--back" aria-label="Biblical affirmation card, verse side">
    <svg class="card-lines" viewBox="0 0 448 716" aria-hidden="true">
      <rect x="47" y="48" width="354" height="619" rx="12" fill="none" stroke="var(--ink)" stroke-width="1.3"/>
      <g class="divider" stroke="var(--ink)">
        <line x1="67" y1="579" x2="196" y2="579" stroke-width="1"/>
        <line x1="253" y1="579" x2="382" y2="579" stroke-width="1"/>
        <line x1="224" y1="540" x2="224" y2="617" stroke-width="1.8"/>
        <line x1="200" y1="564" x2="248" y2="564" stroke-width="1.6"/>
      </g>
    </svg>
    <h2 class="verse-reference">Romans 8:28</h2>
    <p class="verse-text">"And we know that<br>for those who love<br>God all things work<br>together for good,<br>for those who are<br>called according to<br>His purpose."</p>
  </section>

</main>
</body>
</html>
```